Business Card Design

We need a new buisness card designed for a new company in Darwin
We dig trenchs and lay pipes for the communication industry,Electrical industry, Teleco industry,
We also do some concrete works as well,
And small excavation work
Communication
Belvanti Contracting PTY LTD
Pit and Pipe installations
Trenching,Excavations, Concreting ,
civil works, unistrut soloutions ,over thirty years experiance
WHERE NOT FAZED WE WILL LAY ANYTHING
Contact Glen 0491536208 ps
(would like name to stand out somehow in another text or graphic sort of a way am also looking for some sort of slogan) will most likely be a red card with black writing

```html
<!DOCTYPE html>
<html lang="en">
<head>
<meta charset="utf-8">
<title>Belvanti Contracting PTY LTD – Business Card</title>
<link rel="stylesheet" href="https://fonts.googleapis.com/css2?family=Abril+Fatface&family=Arimo:wght@700&family=Roboto+Slab:wght@800&family=Roboto:wght@400&display=swap">
<style>
  :root {
    --card-red: #c8101a;
    --card-red-light: #f2404a;
    --card-red-deep: #6e0208;
    --ink: #141010;
    --ink-soft: #2a0c0c;
    --slogan-grey: #d4d0d0;
    --white: #ffffff;
  }
  html, body {
    margin: 0;
    padding: 0;
    width: 1200px;
    height: 686px;
    overflow: hidden;
    background: var(--card-red-deep);
  }
  .card {
    position: relative;
    width: 1200px;
    height: 686px;
    overflow: hidden;
  }
  .card-texture {
    position: absolute;
    inset: 0;
    background:
      radial-gradient(ellipse 60% 55% at 52% 30%, var(--card-red-light) 0%, var(--card-red) 45%, transparent 80%),
      radial-gradient(ellipse 90% 90% at 50% 45%, var(--card-red) 0%, var(--card-red-deep) 100%);
  }
  .company-name {
    position: absolute;
    left: 0;
    width: 1250px;
    top: 170px;
    margin: 0;
    text-align: center;
    font-family: "Abril Fatface", serif;
    font-weight: 400;
    font-size: 52px;
    line-height: 1;
    color: var(--ink);
    letter-spacing: 0.5px;
  }
  .company-suffix {
    position: absolute;
    left: 353px;
    width: 521px;
    top: 226px;
    display: flex;
    align-items: center;
    gap: 8px;
    font-family: "Arimo", sans-serif;
    font-size: 19px;
    color: var(--ink);
    letter-spacing: 1px;
  }
  .company-suffix .rule {
    flex: 1;
    height: 2px;
    background: var(--ink);
  }
  .company-suffix .rule:first-child { flex: 1.4; }
  .services {
    position: absolute;
    left: 96px;
    top: 284px;
    margin: 0;
    padding: 0;
    list-style: none;
    font-family: "Arimo", sans-serif;
    font-size: 28px;
    color: var(--ink-soft);
    text-shadow: 1px 1px 1px rgba(255,255,255,0.25);
  }
  .services li {
    display: flex;
    align-items: center;
    height: 43px;
  }
  .services .check {
    width: 15px;
    height: 15px;
    margin-right: 6px;
    background: var(--white);
    border: 2px solid var(--ink);
    flex: none;
  }
  .experience {
    position: absolute;
    left: 0;
    width: 1250px;
    top: 410px;
    margin: 0;
    text-align: center;
    font-family: "Arimo", sans-serif;
    font-size: 35px;
    color: var(--ink-soft);
  }
  .slogan {
    position: absolute;
    left: 189px;
    width: 902px;
    top: 462px;
    margin: 0;
    text-align: center;
    font-family: "Roboto Slab", serif;
    font-weight: 800;
    font-size: 33px;
    color: var(--slogan-grey);
    white-space: nowrap;
  }
  .contact {
    position: absolute;
    left: 430px;
    top: 532px;
    display: flex;
    align-items: flex-start;
  }
  .contact-icon {
    width: 72px;
    height: 80px;
    flex: none;
  }
  .contact-text {
    margin-left: -22px;
    color: var(--white);
  }
  .contact-name {
    display: block;
    font-family: "Arimo", sans-serif;
    font-size: 32px;
    line-height: 38px;
  }
  .contact-phone {
    display: block;
    margin-left: 26px;
    font-family: "Roboto", sans-serif;
    font-weight: 400;
    font-size: 42px;
    line-height: 46px;
    letter-spacing: 1px;
  }
</style>
</head>
<body>
<main class="card">
  <div class="card-texture" role="img" aria-label="Red embossed metallic texture background"></div>

  <h1 class="company-name">Belvanti Contracting</h1>
  <div class="company-suffix">
    <span class="rule"></span>
    <span class="suffix-text">PTY LTD</span>
    <span class="rule"></span>
  </div>

  <ul class="services">
    <li><span class="check"></span>Pit and Pipe installations Trenching</li>
    <li><span class="check"></span>Excavations</li>
    <li><span class="check"></span>concreting civil works</li>
  </ul>

  <p class="experience">over thirty years experiance</p>
  <p class="slogan">WHERE NOT FAZED WE WILL LAY ANYTHING</p>

  <div class="contact">
    <svg class="contact-icon" viewBox="0 0 72 80" aria-hidden="true">
      <g fill="none" stroke="#ffffff" stroke-width="5" stroke-linecap="round">
        <path d="M14 14 L40 44"/>
        <path d="M30 6 L50 28" />
      </g>
      <g fill="#ffffff">
        <rect x="8" y="8" width="26" height="14" rx="4" transform="rotate(45 21 15)"/>
        <rect x="34" y="34" width="26" height="14" rx="4" transform="rotate(45 47 41)"/>
      </g>
      <path d="M40 52 C30 60 18 54 10 60 C2 66 6 76 16 74 C26 72 22 62 14 66"
            fill="none" stroke="#ffffff" stroke-width="3" stroke-linecap="round"/>
    </svg>
    <div class="contact-text">
      <span class="contact-name">Contact Glen</span>
      <span class="contact-phone">0491536208</span>
    </div>
  </div>
</main>
</body>
</html>
```